Retirement maintenance and reinstatment brochure

We are looking for a capability statement/brochure outlining our skills and capabilities for maintenance, reinstatement and refurbishment work specific to the requirements of retirement villages in Australia

We are a new company, however our people have significant experience working in this industry

Target Market(s)

Retirement living facilities, aged care facilities, hospitals

Industry/Entity Type

Building

Colors

Designer to choose colors to be used in the design.

Requirements
Must have
• Not alot of wording. Stock images of building refurbishment to retirement living and aged care (carpenters, painters etc)
Nice to have
• 1-2 pages only
Should not have
• alot of meaningless writing

```html
<!DOCTYPE html>
<html lang="en">
<head>
<meta charset="utf-8">
<title>Swift Care Maintenance – Capability Brochure</title>
<link rel="stylesheet" href="https://fonts.googleapis.com/css2?family=Montserrat:wght@400;500;600;700&display=swap">
<style>
  :root {
    --navy: #1f4a86;
    --red: #c8202f;
    --slate: #78797c;
    --ink: #2d4d80;
    --paper: #ffffff;
    --backdrop: #e6e7ea;
  }
  * { box-sizing: border-box; margin: 0; padding: 0; }
  html, body { width: 1200px; height: 800px; overflow: hidden; }
  body {
    background: var(--backdrop);
    font-family: "Montserrat", Arial, sans-serif;
    position: relative;
  }
  .page {
    position: absolute;
    top: 46px;
    width: 500px;
    height: 707px;
    background: var(--paper);
    overflow: hidden;
    box-shadow: 0 4px 14px rgba(0,0,0,0.12);
  }
  .page--back { left: 80px; }
  .page--front { left: 620px; }

  /* Back page */
  .intro-band {
    position: absolute; top: 28px; left: 0; width: 475px; height: 190px;
    background: var(--slate);
    color: #fff; font-size: 13.5px; line-height: 1.45;
    padding: 30px 26px 0 30px;
  }
  .intro-strip {
    position: absolute; top: 28px; left: 475px; width: 25px; height: 190px;
    background: var(--navy);
  }
  .promise {
    position: absolute; left: 34px; top: 250px; width: 165px;
    font-size: 14px; line-height: 1.25; color: var(--ink);
  }
  .promise strong { color: var(--red); font-weight: 700; }
  .compliance {
    position: absolute; left: 34px; top: 355px; width: 215px;
    font-size: 14px; line-height: 1.3; color: var(--ink);
  }
  .trades {
    position: absolute; left: 252px; top: 236px; width: 228px;
    z-index: 2;
  }
  .trades__title {
    background: var(--navy); color: #fff;
    font-size: 11.5px; font-weight: 700; letter-spacing: 0.04em;
    text-transform: uppercase; padding: 8px 12px;
  }
  .trades__list {
    background: var(--red); color: #fff; list-style: none;
    font-size: 12px; line-height: 1.3; padding: 9px 10px 10px 13px;
  }
  .trades__list li {
    position: relative; padding-left: 15px; margin-bottom: 2px;
    white-space: nowrap;
  }
  .trades__list li:last-child { margin-bottom: 0; }
  .trades__list li::before {
    content: ""; position: absolute; left: 0; top: 5px;
    width: 6px; height: 6px; background: #fff;
  }
  .back-photo {
    position: absolute; left: 0; top: 452px; width: 500px; height: 255px;
    background: linear-gradient(160deg, #9fb3c9 0%, #7f8d9c 45%, #c9ccd0 100%);
  }
  .band-shape { position: absolute; left: 0; display: block; }
  .contact {
    position: absolute; right: 0; top: 545px; width: 245px;
    background: var(--navy); color: #fff; text-align: right;
    padding: 12px 14px;
  }
  .contact__title { font-size: 15px; font-weight: 700; letter-spacing: 0.03em; margin-bottom: 4px; }
  .contact__line { font-size: 11px; font-weight: 500; line-height: 1.35; }

  /* Front page */
  .front-photo {
    position: absolute; left: 0; top: 0; width: 500px; height: 500px;
    background: linear-gradient(180deg, #4d7fc4 0%, #8fb2dd 40%, #c8a274 75%, #8a7560 100%);
  }
  .brand {
    position: absolute; right: 36px; top: 520px;
    display: flex; align-items: center; gap: 10px;
  }
  .brand__mark { width: 30px; height: 30px; border-radius: 50%; background: var(--navy); }
  .brand__name { font-size: 22px; font-weight: 700; color: var(--red); letter-spacing: 0.01em; }
  .about {
    position: absolute; right: 32px; top: 590px; width: 440px;
    text-align: right; color: var(--ink);
    font-size: 14px; font-weight: 500; line-height: 1.3;
  }
</style>
</head>
<body>

  <section class="page page--back">
    <div class="intro-band">
      <p>We have expertise in retirement living and aged care maintenance works such as cleaning and painting programs, reinstatement works including painting and carpet replacement as well as major refurbishment or upgrade works including kitchen and bathroom works, electrical and air conditioning upgrade works.</p>
    </div>
    <div class="intro-strip"></div>

    <p class="promise">We have the ability to <strong>react quickly</strong> and <strong>complete works</strong> with as little as <strong>24 hours notice</strong></p>

    <p class="compliance">We are licensed and insured, and have a full workplace health and safety compliance system.</p>

    <div class="trades">
      <h2 class="trades__title">Trades we specialise in</h2>
      <ul class="trades__list">
        <li>Painting and building cleaning</li>
        <li>Carpentry and minor repairs</li>
        <li>Plastering and rendering</li>
        <li>Carpet and floor laying</li>
        <li>Electrical</li>
        <li>Plumbing</li>
        <li>Air conditioning upgrades</li>
      </ul>
    </div>

    <div class="back-photo" role="img" aria-label="Photo of a roofer in a hard hat sealing a flat roof with a gas torch"></div>
    <svg class="band-shape" style="top:442px" width="500" height="70" viewBox="0 0 500 70" aria-hidden="true">
      <polygon points="0,0 500,0 500,36 130,12 0,62" fill="#ffffff"/>
      <polygon points="0,48 112,4 140,4 0,66" fill="#1f4a86"/>
      <polygon points="112,4 500,22 500,44 135,16" fill="#c8202f"/>
    </svg>

    <div class="contact">
      <p class="contact__title">CONTACT US NOW!</p>
      <p class="contact__line">PHONE +61 2000 4821</p>
      <p class="contact__line">EMAIL info@swiftcaremaint.com.au</p>
    </div>
  </section>

  <section class="page page--front">
    <div class="front-photo" role="img" aria-label="Photo of a carpenter fixing timber roof trusses against a blue sky"></div>
    <svg class="band-shape" style="top:370px" width="500" height="140" viewBox="0 0 500 140" aria-hidden="true">
      <polygon points="0,78 110,128 500,58 500,140 0,140" fill="#ffffff"/>
      <polygon points="0,52 140,118 110,128 0,78" fill="#1f4a86"/>
      <polygon points="96,116 500,30 500,58 110,128" fill="#c8202f"/>
    </svg>

    <div class="brand">
      <span class="brand__mark"></span>
      <span class="brand__name">SWIFT CARE MAINTENANCE</span>
    </div>

    <p class="about">Swift Care Maintenance is a commercial building and maintenance company established and located on the Sunshine Coast in QLD.</p>
  </section>

</body>
</html>
```